brisk-vale.com Real Estate, Investment, Financial corporate

Real Estate, Investment, Financial corporate looking site. Show present a professional firm, with an elegant display. Please see the attached file which includes the logo, palette and fonts.
Updates

We just starting the brief today. ( logo was delayed)

Target Market(s)

Investors, Corporate , B2b

Industry/Entity Type

real-estate investments

Number of Pages Required

3 page

Requirements
Must have
• Dazzling Homepage
Nice to have
• paralex

```html
<!DOCTYPE html>
<html lang="en">
<head>
<meta charset="utf-8">
<title>Brisk Vale Real Estate</title>
<link href="https://fonts.googleapis.com/css2?family=Montserrat:wght@400;500;600;700;800&family=Open+Sans:wght@400;600&display=swap" rel="stylesheet">
<style>
:root{
  --blue:#1f6fd8;
  --blue-dark:#1559b3;
  --ink:#1d232b;
  --text:#4b525a;
  --muted:#8a9096;
  --line:#e3e6ea;
  --bg:#ffffff;
  --soft:#f5f7f9;
  --footer:#2a2c2f;
  --footer-text:#b8bcc1;
}
*{margin:0;padding:0;box-sizing:border-box}
html,body{width:1200px;height:2356px;overflow:hidden}
body{background:var(--bg);font-family:'Open Sans',Arial,sans-serif;color:var(--text);position:relative}
h1,h2,h3,h4,.btn,.nav a,.brand{font-family:'Montserrat',Arial,sans-serif}
.btn{display:inline-block;background:var(--blue);color:#fff;font-size:10px;font-weight:700;letter-spacing:.6px;text-transform:uppercase;padding:9px 16px;border-radius:2px;text-decoration:none}

/* header */
.site-header{position:absolute;top:0;left:0;width:1200px;height:56px;background:#fff;display:flex;align-items:center;padding:0 60px;justify-content:space-between;box-shadow:0 1px 6px rgba(0,0,0,.06);z-index:2}
.brand{font-weight:600;font-size:15px;color:var(--ink);white-space:nowrap}
.nav{display:flex;align-items:center;gap:40px;margin-right:120px}
.nav a{font-size:10px;font-weight:600;letter-spacing:.8px;color:var(--ink);text-decoration:none;text-transform:uppercase}
.nav a.active{color:var(--blue);border-bottom:2px solid var(--blue);padding-bottom:4px}

/* hero */
.hero{position:absolute;top:56px;left:0;width:1200px;height:392px;background:linear-gradient(100deg,#4f7fb4 0%,#86add3 35%,#c9d7e3 60%,#e9ecee 75%,#9aa4ad 100%)}
.hero-shade{position:absolute;inset:0;background:linear-gradient(90deg,rgba(15,30,50,.45),rgba(15,30,50,0) 55%)}
.hero-copy{position:absolute;left:60px;top:116px;color:#fff}
.hero-copy h1{font-size:38px;font-weight:800;line-height:1.1;letter-spacing:.5px}
.hero-copy p{font-size:11px;line-height:1.6;margin:14px 0 18px;width:300px;opacity:.9}

/* search */
.search{position:absolute;top:470px;left:140px;width:920px;height:44px;background:#fff;box-shadow:0 4px 16px rgba(0,0,0,.1);display:flex;align-items:center;padding:0 12px;gap:12px}
.select{flex:1;height:26px;border:1px solid var(--line);border-radius:2px;font-size:10px;color:var(--muted);display:flex;align-items:center;justify-content:space-between;padding:0 10px}
.select svg{width:8px;height:8px}
.search .btn{padding:7px 22px}

/* listings */
.listings{position:absolute;top:532px;left:220px;width:760px;display:grid;grid-template-columns:repeat(3,240px);column-gap:20px;row-gap:40px}
.card{background:#fff;box-shadow:0 2px 10px rgba(0,0,0,.08);height:328px}
.card-photo{height:200px;position:relative}
.tag{position:absolute;right:8px;bottom:8px;background:rgba(20,24,30,.8);color:#fff;font-size:8px;font-weight:600;padding:3px 7px;letter-spacing:.5px}
.card-body{padding:12px 14px}
.card-title{font-family:'Montserrat',Arial,sans-serif;font-size:11px;font-weight:700;color:var(--ink);text-align:center;text-transform:uppercase;line-height:1.4;height:32px}
.card-meta{display:flex;justify-content:space-between;margin-top:14px}
.facts{list-style:none;font-size:9px;color:var(--muted)}
.facts li{display:flex;align-items:center;gap:6px;margin-bottom:5px}
.facts svg{width:9px;height:9px}
.deal{text-align:right}
.price{font-family:'Montserrat',Arial,sans-serif;font-size:11px;font-weight:700;color:var(--ink);margin-bottom:8px}
.deal .btn{padding:7px 12px;font-size:9px}
.see-more{position:absolute;top:1284px;left:0;width:1200px;text-align:center;font-family:'Montserrat',Arial,sans-serif;font-size:9px;font-weight:700;color:var(--blue);letter-spacing:.8px}

/* newsletter band */
.band{position:absolute;top:1332px;left:0;width:1200px;height:220px;background:linear-gradient(90deg,#15181c,#3a3530 45%,#2a2722 70%,#111315)}
.band-copy{position:absolute;top:46px;width:100%;text-align:center;color:#fff}
.band-copy h2{font-size:24px;font-weight:800;letter-spacing:.5px}
.band-copy p{font-size:10px;opacity:.75;margin-top:6px}
.subscribe{display:flex;justify-content:center;margin-top:20px}
.subscribe .field{width:300px;height:32px;background:#fff;font-size:10px;color:var(--muted);display:flex;align-items:center;padding:0 12px}
.subscribe .btn{height:32px;padding:11px 18px}

/* reasons */
.reasons-title{position:absolute;top:1620px;left:0;width:1200px;text-align:center;font-size:20px;font-weight:800;color:var(--ink)}
.reasons{position:absolute;top:1688px;left:220px;display:grid;grid-template-columns:repeat(3,240px);column-gap:20px}
.reason{background:#fff;box-shadow:0 2px 10px rgba(0,0,0,.08);height:244px}
.reason-photo{height:140px}
.reason-body{padding:14px 16px;text-align:center}
.reason-body h3{font-size:9px;font-weight:700;color:var(--ink);letter-spacing:.6px;text-transform:uppercase}
.reason-body p{font-size:9px;line-height:1.6;margin-top:8px;color:var(--muted)}

/* feature */
.feature-photo{position:absolute;top:1960px;left:220px;width:380px;height:260px}
.feature-copy{position:absolute;top:2008px;left:640px;width:340px}
.feature-copy h2{font-size:24px;font-weight:800;color:var(--ink);line-height:1.2;text-transform:uppercase}
.feature-copy p{font-size:10px;line-height:1.7;color:var(--muted);margin:14px 0 16px}

/* footer */
.site-footer{position:absolute;top:2264px;left:0;width:1200px;height:92px;background:var(--footer);color:var(--footer-text);padding:14px 60px;display:flex}
.site-footer .brand{color:#fff;font-size:14px}
.foot-about{width:500px}
.foot-about p{font-size:8px;line-height:1.6;margin:8px 0;width:300px}
.socials{display:flex;gap:6px}
.socials span{width:12px;height:12px;background:var(--footer-text);border-radius:2px}
.foot-links{width:160px}
.site-footer h4{font-size:8px;font-weight:700;color:#fff;letter-spacing:.6px;margin-bottom:6px;text-transform:uppercase}
.foot-links ul{list-style:none;font-size:8px;line-height:1.7}
.foot-news p{font-size:8px;line-height:1.6;width:280px}
.foot-news .row{display:flex;margin-top:6px}
.foot-news .field{width:200px;height:22px;background:#fff;font-size:8px;color:var(--muted);display:flex;align-items:center;padding:0 8px}
.foot-news .btn{padding:6px 12px;font-size:8px}
</style>
</head>
<body>

<header class="site-header">
  <div class="brand">Brisk Vale</div>
  <nav class="nav">
    <a class="active" href="#">Home</a>
    <a href="#">Properties</a>
    <a href="#">About Us</a>
    <a class="btn" href="#" style="color:#fff">Contact Us</a>
  </nav>
</header>

<section class="hero" role="img" aria-label="Modern two-storey white house with large glass windows under a blue sky">
  <div class="hero-shade"></div>
  <div class="hero-copy">
    <h1>FIND YOUR<br>FUTURE HOME</h1>
    <p>We help you find the right property to live in or invest in, with trusted guidance at every step.</p>
    <a class="btn" href="#">Contact Us</a>
  </div>
</section>

<form class="search">
  <div class="select">Location<svg viewBox="0 0 8 8"><path d="M1 2.5l3 3 3-3" fill="none" stroke="#8a9096" stroke-width="1.2"/></svg></div>
  <div class="select">Property Type<svg viewBox="0 0 8 8"><path d="M1 2.5l3 3 3-3" fill="none" stroke="#8a9096" stroke-width="1.2"/></svg></div>
  <div class="select">Price Range<svg viewBox="0 0 8 8"><path d="M1 2.5l3 3 3-3" fill="none" stroke="#8a9096" stroke-width="1.2"/></svg></div>
  <div class="select">Beds<svg viewBox="0 0 8 8"><path d="M1 2.5l3 3 3-3" fill="none" stroke="#8a9096" stroke-width="1.2"/></svg></div>
  <a class="btn" href="#">Search</a>
</form>

<main class="listings">
  <article class="card">
    <div class="card-photo" role="img" aria-label="Dark modern house with timber cladding at dusk" style="background:linear-gradient(160deg,#3b5f8e,#22303f 60%,#5b4a3a)"></div>
    <div class="card-body">
      <h3 class="card-title">14 Linden Hollow<br>Fairmead</h3>
      <div class="card-meta">
        <ul class="facts">
          <li><svg viewBox="0 0 9 9"><rect x="1" y="1" width="7" height="7" fill="none" stroke="#8a9096"/></svg>4 Bedrooms</li>
          <li><svg viewBox="0 0 9 9"><rect x="1" y="1" width="7" height="7" fill="none" stroke="#8a9096"/></svg>3 Baths</li>
          <li><svg viewBox="0 0 9 9"><rect x="1" y="1" width="7" height="7" fill="none" stroke="#8a9096"/></svg>2,400 sqft</li>
        </ul>
        <div class="deal"><div class="price">$ 1,890 USD</div><a class="btn" href="#">View Details</a></div>
      </div>
    </div>
  </article>
  <article class="card">
    <div class="card-photo" role="img" aria-label="Contemporary villa lit warmly at evening among trees" style="background:linear-gradient(160deg,#2d3a48,#4a4234 55%,#7a5f3c)"></div>
    <div class="card-body">
      <h3 class="card-title">5120 Harbor Crest Road<br>Coveport</h3>
      <div class="card-meta">
        <ul class="facts">
          <li><svg viewBox="0 0 9 9"><rect x="1" y="1" width="7" height="7" fill="none" stroke="#8a9096"/></svg>5 Bedrooms</li>
          <li><svg viewBox="0 0 9 9"><rect x="1" y="1" width="7" height="7" fill="none" stroke="#8a9096"/></svg>4 Baths</li>
          <li><svg viewBox="0 0 9 9"><rect x="1" y="1" width="7" height="7" fill="none" stroke="#8a9096"/></svg>3,100 sqft</li>
        </ul>
        <div class="deal"><div class="price">$ 2,450 USD</div><a class="btn" href="#">View Details</a></div>
      </div>
    </div>
  </article>
  <article class="card">
    <div class="card-photo" role="img" aria-label="Single-storey house with a green lawn under a clear sky" style="background:linear-gradient(180deg,#8fb6dc,#c8d6cf 50%,#5f8c45)"><span class="tag">For Sale</span></div>
    <div class="card-body">
      <h3 class="card-title">302 Sunridge Lane<br>Alder Bay</h3>
      <div class="card-meta">
        <ul class="facts">
          <li><svg viewBox="0 0 9 9"><rect x="1" y="1" width="7" height="7" fill="none" stroke="#8a9096"/></svg>3 Bedrooms</li>
          <li><svg viewBox="0 0 9 9"><rect x="1" y="1" width="7" height="7" fill="none" stroke="#8a9096"/></svg>2 Baths</li>
          <li><svg viewBox="0 0 9 9"><rect x="1" y="1" width="7" height="7" fill="none" stroke="#8a9096"/></svg>1,850 sqft</li>
        </ul>
        <div class="deal"><div class="price">$ 1,690 USD</div><a class="btn" href="#">View Details</a></div>
      </div>
    </div>
  </article>
  <article class="card">
    <div class="card-photo" role="img" aria-label="White cottage with red roof and autumn trees" style="background:linear-gradient(180deg,#b9cbd8,#d8c8a8 50%,#8a6a3e)"><span class="tag">For Sale</span></div>
    <div class="card-body">
      <h3 class="card-title">918 Orchard Row<br>Maple Glen</h3>
      <div class="card-meta">
        <ul class="facts">
          <li><svg viewBox="0 0 9 9"><rect x="1" y="1" width="7" height="7" fill="none" stroke="#8a9096"/></svg>3 Bedrooms</li>
          <li><svg viewBox="0 0 9 9"><rect x="1" y="1" width="7" height="7" fill="none" stroke="#8a9096"/></svg>2 Baths</li>
          <li><svg viewBox="0 0 9 9"><rect x="1" y="1" width="7" height="7" fill="none" stroke="#8a9096"/></svg>1,640 sqft</li>
        </ul>
        <div class="deal"><div class="price">$ 1,250 USD</div><a class="btn" href="#">View Details</a></div>
      </div>
    </div>
  </article>
  <article class="card">
    <div class="card-photo" role="img" aria-label="Red brick family house on a wide lawn at sunset" style="background:linear-gradient(180deg,#9fb3c4,#8c5a42 55%,#4d6b34)"><span class="tag">For Sale</span></div>
    <div class="card-body">
      <h3 class="card-title">461 Kestrel Point<br>Rowanfield</h3>
      <div class="card-meta">
        <ul class="facts">
          <li><svg viewBox="0 0 9 9"><rect x="1" y="1" width="7" height="7" fill="none" stroke="#8a9096"/></svg>4 Bedrooms</li>
          <li><svg viewBox="0 0 9 9"><rect x="1" y="1" width="7" height="7" fill="none" stroke="#8a9096"/></svg>3 Baths</li>
          <li><svg viewBox="0 0 9 9"><rect x="1" y="1" width="7" height="7" fill="none" stroke="#8a9096"/></svg>2,780 sqft</li>
        </ul>
        <div class="deal"><div class="price">$ 8,000 USD</div><a class="btn" href="#">View Details</a></div>
      </div>
    </div>
  </article>
  <article class="card">
    <div class="card-photo" role="img" aria-label="Modern house with lit interior at twilight" style="background:linear-gradient(170deg,#2a3c57,#4a5a6e 50%,#b98a4f)"></div>
    <div class="card-body">
      <h3 class="card-title">77 Meadowbank Court<br>Fairmead</h3>
      <div class="card-meta">
        <ul class="facts">
          <li><svg viewBox="0 0 9 9"><rect x="1" y="1" width="7" height="7" fill="none" stroke="#8a9096"/></svg>5 Bedrooms</li>
          <li><svg viewBox="0 0 9 9"><rect x="1" y="1" width="7" height="7" fill="none" stroke="#8a9096"/></svg>4 Baths</li>
          <li><svg viewBox="0 0 9 9"><rect x="1" y="1" width="7" height="7" fill="none" stroke="#8a9096"/></svg>3,400 sqft</li>
        </ul>
        <div class="deal"><div class="price">$ 1,980 USD</div><a class="btn" href="#">View Details</a></div>
      </div>
    </div>
  </article>
</main>

<div class="see-more">SEE MORE PROPERTIES &#8594;</div>

<section class="band" role="img" aria-label="Dimmed evening view of a luxury house exterior">
  <div class="band-copy">
    <h2>BE THE FIRST TO MEET YOUR DREAM<br>HOUSE</h2>
    <p>Get new listings sent to your inbox before anyone else.</p>
    <div class="subscribe"><div class="field">Your email address</div><a class="btn" href="#">Subscribe</a></div>
  </div>
</section>

<h2 class="reasons-title">WHAT MAKE US THE BEST REAL ESTATE FIRM</h2>

<section class="reasons">
  <article class="reason">
    <div class="reason-photo" role="img" aria-label="Turquoise beach with resort buildings" style="background:linear-gradient(160deg,#6fc2d6,#2f8fa8 50%,#d9c9a3)"></div>
    <div class="reason-body"><h3>Exclusive Properties</h3><p>Access homes and estates you will not find on public listings anywhere else.</p></div>
  </article>
  <article class="reason">
    <div class="reason-photo" role="img" aria-label="Agent working at a laptop in an office" style="background:linear-gradient(160deg,#2f3a46,#6c7782 55%,#c9ccd0)"></div>
    <div class="reason-body"><h3>Best Agents</h3><p>Skilled advisors who know each market and guide every deal with care.</p></div>
  </article>
  <article class="reason">
    <div class="reason-photo" role="img" aria-label="Clients meeting with an advisor at a table" style="background:linear-gradient(160deg,#d9d4cc,#a89a88 55%,#6d5f52)"></div>
    <div class="reason-body"><h3>Expert Clients</h3><p>Investors and firms trust us to build strong and lasting portfolios.</p></div>
  </article>
</section>

<div class="feature-photo" role="img" aria-label="Modern white villa with a pool at dusk" style="background:linear-gradient(180deg,#8fa9c4,#d8d2c6 45%,#3f8fb0 80%,#2a6a86)"></div>
<section class="feature-copy">
  <h2>Helping people to find their dream house</h2>
  <p>For over two decades we have matched families and investors with the right homes. Our team handles research, viewings and paperwork so you can move forward with full confidence.</p>
  <a class="btn" href="#">Contact Us</a>
</section>

<footer class="site-footer">
  <div class="foot-about">
    <div class="brand">Brisk Vale</div>
    <p>A trusted real estate and investment firm serving buyers, sellers and partners. brisk-vale.com</p>
    <div class="socials"><span></span><span></span><span></span></div>
  </div>
  <div class="foot-links">
    <h4>Quick Links</h4>
    <ul><li>Properties</li><li>About Us</li><li>Privacy Policy</li><li>Terms &amp; Conditions</li></ul>
  </div>
  <div class="foot-news">
    <h4>Be the first to meet your dream house</h4>
    <p>Sign up to receive our latest listings and market news.</p>
    <div class="row"><div class="field">Your email</div><a class="btn" href="#">Subscribe</a></div>
  </div>
</footer>

</body>
</html>
```